Cardiology practice business card

We need a business card for our cardiology practice "Bellmoor Cardiology". We have a new logo, attached below. We like the colours in the logo - red and charcoal. The front of the business card will need to have the doctors name, address, phone number and email. The back will need to have space to write 2 appointment dates and times.

```html
<!DOCTYPE html>
<html lang="en">
<head>
<meta charset="utf-8">
<title>Bellmoor Cardiology – Business Card</title>
<link href="https://fonts.googleapis.com/css2?family=Montserrat:wght@500;600;700&display=swap" rel="stylesheet">
<style>
  :root {
    --backdrop: #d7d5d6;
    --card: #ffffff;
    --red: #d8131b;
    --charcoal: #6d6e71;
    --rule: #7a7b7e;
    --line-light: #b9babd;
  }
  * { margin: 0; padding: 0; box-sizing: border-box; }
  html, body {
    width: 1200px; height: 1109px; overflow: hidden;
    background: var(--backdrop);
    font-family: "Montserrat", Arial, sans-serif;
  }
  .card {
    position: absolute; left: 216px; width: 768px; height: 440px;
    background: var(--card);
  }
  .card--front { top: 71px; }
  .card--back { top: 570px; }

  .brand {
    position: absolute; display: flex; align-items: center; gap: 14px;
  }
  .brand__dot {
    width: 18px; height: 18px; border-radius: 50%; background: var(--red); flex: none;
  }
  .brand__name {
    color: var(--red); font-weight: 700; font-size: 30px; line-height: 1.12;
    letter-spacing: 1.5px; text-transform: uppercase;
  }
  .card--front .brand { left: 70px; top: 140px; }
  .card--back .brand { left: 60px; top: 172px; }
  .card--back .brand__name { font-size: 27px; }

  .front-accent {
    position: absolute; left: 470px; top: 94px; width: 300px; height: 300px;
  }

  .appointments {
    position: absolute; left: 70px; top: 240px; width: 340px;
    color: var(--charcoal);
  }
  .appointments__title {
    color: var(--red); font-weight: 600; font-size: 13px; letter-spacing: 2.6px;
    text-transform: uppercase; margin-bottom: 14px;
  }
  .appointments__row {
    display: flex; align-items: flex-end; gap: 10px; height: 30px; margin-bottom: 8px;
    font-weight: 600; font-size: 13px; letter-spacing: 0.8px;
  }
  .appointments__blank {
    flex: 1; border-bottom: 1.5px solid var(--line-light); height: 18px;
  }
  .appointments__blank--time { flex: 0 0 80px; }

  .divider {
    position: absolute; left: 384px; top: 70px; width: 2px; height: 300px;
    background: var(--rule);
  }
  .person { position: absolute; left: 416px; top: 72px; }
  .person__name {
    color: var(--charcoal); font-weight: 600; font-size: 50px; letter-spacing: -1.5px; line-height: 1;
  }
  .person__role {
    margin-top: 8px; color: var(--red); font-weight: 600; font-size: 16px; letter-spacing: 3.2px;
  }
  .person__rule {
    margin-top: 11px; width: 180px; height: 2px; background: var(--rule);
  }
  .contacts { position: absolute; left: 422px; top: 184px; list-style: none; }
  .contacts__item {
    display: flex; align-items: center; height: 26px; margin-bottom: 21px;
    color: var(--charcoal); font-weight: 600; font-size: 17px; letter-spacing: 1.1px;
    white-space: nowrap;
  }
  .contacts__icon { width: 26px; height: 26px; margin-right: 19px; flex: none; }
</style>
</head>
<body>
  <section class="card card--front">
    <div class="brand">
      <span class="brand__dot"></span>
      <span class="brand__name">Bellmoor<br>Cardiology</span>
    </div>
    <div class="appointments">
      <p class="appointments__title">Your appointments</p>
      <div class="appointments__row">
        <span>Date</span><span class="appointments__blank"></span>
        <span>Time</span><span class="appointments__blank appointments__blank--time"></span>
      </div>
      <div class="appointments__row">
        <span>Date</span><span class="appointments__blank"></span>
        <span>Time</span><span class="appointments__blank appointments__blank--time"></span>
      </div>
    </div>
    <svg class="front-accent" viewBox="0 0 300 300" aria-hidden="true">
      <circle cx="150" cy="150" r="144" fill="none" stroke="var(--red)" stroke-width="5"/>
    </svg>
  </section>

  <section class="card card--back">
    <div class="brand">
      <span class="brand__dot"></span>
      <span class="brand__name">Bellmoor<br>Cardiology</span>
    </div>
    <div class="divider"></div>
    <div class="person">
      <h1 class="person__name">Dr Hale</h1>
      <p class="person__role">DESIGNATION</p>
      <div class="person__rule"></div>
    </div>
    <ul class="contacts">
      <li class="contacts__item">
        <svg class="contacts__icon" viewBox="0 0 26 26" aria-hidden="true">
          <circle cx="13" cy="13" r="13" fill="var(--red)"/>
          <path d="M9 7.5l2 0 1.2 3-1.5 1.1a7 7 0 0 0 3.7 3.7l1.1-1.5 3 1.2v2a1.6 1.6 0 0 1-1.7 1.5A10 10 0 0 1 7.5 9.2 1.6 1.6 0 0 1 9 7.5z" fill="#fff"/>
        </svg>
        +070 5120 43981
      </li>
      <li class="contacts__item">
        <svg class="contacts__icon" viewBox="0 0 26 26" aria-hidden="true">
          <circle cx="13" cy="13" r="13" fill="var(--red)"/>
          <rect x="7" y="9" width="12" height="8.5" fill="#fff"/>
          <path d="M7 9l6 5 6-5M7 17.5l4.5-4.2M19 17.5l-4.5-4.2" fill="none" stroke="var(--red)" stroke-width="1"/>
        </svg>
        hello@bellmoorheart.com
      </li>
      <li class="contacts__item">
        <svg class="contacts__icon" viewBox="0 0 26 26" aria-hidden="true">
          <circle cx="13" cy="13" r="13" fill="var(--red)"/>
          <g fill="none" stroke="#fff" stroke-width="1.4">
            <circle cx="13" cy="13" r="7"/>
            <ellipse cx="13" cy="13" rx="3" ry="7"/>
            <path d="M6 13h14M7 9.5h12M7 16.5h12"/>
          </g>
        </svg>
        www.bellmoorheart.com
      </li>
      <li class="contacts__item">
        <svg class="contacts__icon" viewBox="0 0 26 26" aria-hidden="true">
          <circle cx="13" cy="13" r="13" fill="var(--red)"/>
          <path d="M13 6a5 5 0 0 0-5 5c0 3.8 5 9 5 9s5-5.2 5-9a5 5 0 0 0-5-5z" fill="#fff"/>
          <circle cx="13" cy="11" r="1.8" fill="var(--red)"/>
        </svg>
        14 Harrow Lane, Kestford
      </li>
    </ul>
  </section>
</body>
</html>
```